Pediatric Practice Flyer Design

I need marketing flyer created for distribution. It is for a pediatric clinic. Need some realistic eye catching design and content. I already have a logo that will go on top of the flyer. I will be using quellomark for flyer print service. So need it copyable for printing. Again, need eye catching content as well. We are planning on opening the clinic in December.

```html
<!DOCTYPE html>
<html lang="en">
<head>
<meta charset="utf-8">
<title>Meadowlark Kids Care Pediatrics – Opening Soon Flyer</title>
<link rel="stylesheet" href="https://fonts.googleapis.com/css2?family=Fredoka:wght@500;600;700&family=Poppins:wght@400;600&display=swap">
<style>
  :root {
    --stage: #e8e4d9;
    --paper: #ffffff;
    --red: #ea1f2b;
    --orange: #f5941f;
    --purple: #6a2c91;
    --pink: #e5189a;
    --blue: #1b70b8;
    --ink: #222222;
    --white: #ffffff;
  }
  * { box-sizing: border-box; margin: 0; padding: 0; }
  html, body {
    width: 1200px; height: 900px; overflow: hidden;
    background: var(--stage);
  }
  .flyer {
    position: absolute; left: 310px; top: 40px;
    width: 580px; height: 820px;
    background: var(--paper);
    overflow: hidden;
    box-shadow: 0 10px 30px rgba(0,0,0,.12);
  }
  .flyer__header { position: absolute; left: 0; top: 0; width: 580px; height: 420px; }
  .headline-opening {
    position: absolute; left: 0; top: 95px; width: 580px;
    text-align: center;
    font-family: "Fredoka", sans-serif; font-weight: 700;
    font-size: 124px; line-height: .95; letter-spacing: -2px;
    color: var(--white);
    -webkit-text-stroke: 18px var(--orange);
    paint-order: stroke fill;
  }
  .brand {
    position: absolute; left: 60px; top: 420px;
    display: flex; align-items: center; gap: 16px;
  }
  .brand__dot { width: 58px; height: 58px; border-radius: 50%; background: var(--orange); }
  .brand__name {
    font-family: "Fredoka", sans-serif; font-weight: 600;
    font-size: 30px; line-height: 1.05; color: var(--red);
  }
  .tagline {
    position: absolute; left: 80px; top: 498px; width: 420px;
    text-align: center;
    font-family: "Fredoka", sans-serif; font-weight: 700;
    font-size: 40px; line-height: 1.02; color: var(--blue);
  }
  .intro {
    position: absolute; left: 145px; top: 632px; width: 315px;
    text-align: center;
    font-family: "Poppins", sans-serif; font-weight: 400;
    font-size: 13px; line-height: 1.35; color: var(--ink);
  }
  .figure { position: absolute; border-radius: 40px 40px 10px 10px; }
  .figure--left { left: 28px; top: 625px; width: 110px; height: 139px; background: linear-gradient(180deg, #8a4db0, var(--purple)); }
  .figure--right { left: 478px; top: 600px; width: 88px; height: 150px; background: linear-gradient(180deg, #f04fb4, var(--pink)); }
  .ball { position: absolute; left: 20px; top: 580px; width: 42px; height: 42px; border-radius: 50%; background: var(--purple); }
  .footer {
    position: absolute; left: 0; bottom: 0; width: 580px; height: 56px;
    background: var(--purple);
    display: flex; align-items: center;
    font-family: "Poppins", sans-serif; color: var(--white);
  }
  .footer__item { display: flex; align-items: center; gap: 6px; font-size: 15px; }
  .footer__web { width: 220px; justify-content: center; }
  .footer__phone {
    width: 150px; height: 74px; margin-top: -18px;
    background: var(--pink); justify-content: center;
    font-weight: 600; font-size: 17px;
  }
  .footer__address { width: 210px; justify-content: center; }
  .footer svg { width: 14px; height: 14px; fill: rgba(255,255,255,.75); }
</style>
</head>
<body>
  <main class="flyer">
    <svg class="flyer__header" viewBox="0 0 580 420" aria-hidden="true">
      <path d="M0,0 H580 V250 C470,350 260,390 0,385 Z" fill="var(--red)"/>
      <path d="M0,385 C260,390 470,350 580,250 V264 C470,368 260,404 0,404 Z" fill="var(--purple)"/>
      <path d="M0,150 C100,120 175,60 210,0 H228 C190,85 110,155 0,192 Z" fill="var(--orange)"/>
    </svg>
    <h1 class="headline-opening">Opening<br>Soon!</h1>

    <div class="brand">
      <span class="brand__dot"></span>
      <span class="brand__name">Meadowlark Kids<br>Care Pediatrics</span>
    </div>

    <h2 class="tagline">We Believe It<br>Takes A Community<br>To Raise A Child.</h2>

    <div class="ball"></div>
    <div class="figure figure--left" role="img" aria-label="Silhouette illustration of a child reaching up for a ball"></div>
    <div class="figure figure--right" role="img" aria-label="Silhouette illustration of a kneeling child with arms raised"></div>

    <p class="intro">We are excited to be small yet important member of the community to help raise a healthy and happy child. Our goal is to provide personalized and comprehensive care collectively that consists of the parent child and provider triangle</p>

    <footer class="footer">
      <span class="footer__item footer__web">
        <svg viewBox="0 0 24 24"><path d="M12 2a10 10 0 1 0 0 20 10 10 0 0 0 0-20zm0 2c.9 1.2 1.6 2.6 2 4h-4c.4-1.4 1.1-2.8 2-4zM4.3 14a8 8 0 0 1 0-4h3.4a16 16 0 0 0 0 4zm.9 2h3c.3 1.3.8 2.5 1.4 3.6A8 8 0 0 1 5.2 16zm3-8h-3a8 8 0 0 1 4.4-3.6C8.9 5.5 8.5 6.7 8.2 8zM12 20c-.9-1.2-1.6-2.6-2-4h4c-.4 1.4-1.1 2.8-2 4zm2.3-6H9.7a14 14 0 0 1 0-4h4.6a14 14 0 0 1 0 4zm.1 5.6c.6-1.1 1.1-2.3 1.4-3.6h3a8 8 0 0 1-4.4 3.6zm1.9-5.6a16 16 0 0 0 0-4h3.4a8 8 0 0 1 0 4zm-.5-6c-.3-1.300-.8-2.5-1.4-3.6A8 8 0 0 1 18.8 8z"/></svg>
        meadowlarkpeds.com
      </span>
      <span class="footer__item footer__phone">
        <svg viewBox="0 0 24 24"><path d="M6.6 10.8a15 15 0 0 0 6.6 6.6l2.2-2.2c.3-.3.7-.4 1-.2 1.1.4 2.3.6 3.6.6.6 0 1 .4 1 1V20c0 .6-.4 1-1 1A17 17 0 0 1 3 4c0-.6.4-1 1-1h3.5c.6 0 1 .4 1 1 0 1.3.2 2.5.6 3.6.1.3 0 .7-.2 1z"/></svg>
        0198 765 432
      </span>
      <span class="footer__item footer__address">
        <svg viewBox="0 0 24 24"><path d="M12 2a7 7 0 0 0-7 7c0 5.2 7 13 7 13s7-7.8 7-13a7 7 0 0 0-7-7zm0 9.5A2.5 2.5 0 1 1 12 6.5a2.5 2.5 0 0 1 0 5z"/></svg>
        meadowlarkpeds.com
      </span>
    </footer>
  </main>
</body>
</html>
```